Commercial painting company is looking for a creative website designer.

Hi, we just completed our logo project and now ready to launch our website. The project will be done on Squarespace platform. It will contain:
Page 1 HOME
Page 2 SERVICES
Page 3 PICTURES
The content will be written by us. I am not sure bout the pictures, I do not have any to provide. I can buy stock photos if needed.
We are commercial only painting company and have to appeal to commercial, industrial property mangers. We will need CALL, REQUEST FOR ESTIMATE buttons.
If possible to have a live picture on home page would be great. Thank you
Target Market(s)
Property Managers
Industry/Entity Type
Commercial Painting
Other font styles liked:
- Poppins

```html
<!DOCTYPE html>
<html lang="en">
<head>
<meta charset="utf-8">
<title>Brushline Coatings — Commercial Painting</title>
<link href="https://fonts.googleapis.com/css2?family=Barlow:wght@400;500;600&display=swap" rel="stylesheet">
<style>
:root{
  --yellow:#fdc100;
  --black:#000;
  --ink:#111;
  --white:#fff;
  --navy:#1b2438;
  --field:#f1f1f1;
  --muted:#333;
}
*{box-sizing:border-box;margin:0;padding:0}
html,body{width:1200px;height:3545px;overflow:hidden}
body{position:relative;font-family:"Barlow",Arial,sans-serif;color:var(--ink);background:var(--white)}
section,header,footer{position:absolute;left:0;width:1200px}
.abs{position:absolute}
.btn{position:absolute;display:flex;align-items:center;justify-content:center;font-size:17px;font-weight:500;text-transform:uppercase;letter-spacing:.2px}
.btn-yellow{background:var(--yellow);color:var(--black)}
.btn-black{background:var(--black);color:var(--white)}
.btn-send{background:var(--black);color:var(--yellow)}

/* header */
.site-header{top:0;height:79px;background:var(--yellow)}
.brand{left:103px;top:24px;display:flex;align-items:center;gap:10px;font-size:17px;font-weight:600;text-transform:uppercase;color:var(--black)}
.brand-mark{width:28px;height:28px;background:var(--black)}
.nav{top:30px;font-size:17px;font-weight:500;text-transform:uppercase}
.phone{display:flex;align-items:center;gap:7px;font-weight:500}

/* hero */
.hero{top:79px;height:463px;background:linear-gradient(100deg,#4f4c56 0%,#5b5965 45%,#6e8f84 70%,#55606a 100%)}
.hero h1{left:143px;top:113px;font-size:41px;line-height:48px;font-weight:600;color:var(--white);text-transform:uppercase}

/* about */
.about{top:542px;height:530px}
.about h2{left:637px;top:124px;font-size:30px;line-height:33px;font-weight:500}
.about p{left:637px;top:210px;width:400px;font-size:14px;line-height:25px;color:var(--muted)}
.about .phone{position:absolute;left:637px;top:364px;font-size:16px}

/* benefits */
.benefits{top:1072px;height:382px;background:var(--yellow)}
.benefit{top:77px;width:200px;text-align:center}
.benefit-icon{display:block;margin:0 auto 20px}
.benefit p{font-size:16px;line-height:20px;font-weight:500}

/* services */
.services{top:1454px;height:523px;background:linear-gradient(160deg,#2a3347 0%,#1a2234 50%,#131a28 100%)}
.services h2{left:0;width:1200px;top:68px;text-align:center;font-size:30px;font-weight:500;color:var(--yellow);text-transform:uppercase}
.service-card{top:131px;width:207px;height:218px;background:var(--white)}
.service-photo{height:146px}
.service-card span{display:flex;height:72px;align-items:center;justify-content:center;font-size:17px;font-weight:500;text-transform:uppercase}

/* steps */
.steps{top:1977px;height:296px}
.steps h2{left:0;width:1200px;top:52px;text-align:center;font-size:30px;font-weight:500;text-transform:uppercase}
.step{top:142px;display:flex;gap:18px}
.step-icon{width:72px;height:72px;border-radius:50%;background:var(--yellow);display:flex;align-items:center;justify-content:center;flex:none}
.step h3{font-size:20px;font-weight:500;text-transform:uppercase;margin-top:-4px}
.step p{font-size:13px;line-height:16px;width:160px;margin-top:3px}

/* cta */
.cta{top:2273px;height:458px;background:linear-gradient(90deg,#6a7282 0%,#8f96a2 50%,#9aa0aa 100%)}
.cta h2{left:0;width:1200px;top:117px;text-align:center;font-size:30px;font-weight:500;color:var(--white);text-transform:uppercase}
.cta p{left:285px;width:630px;top:188px;text-align:center;font-size:14px;line-height:25px;color:var(--white)}

/* contact */
.contact{top:2731px;height:574px}
.contact-band{left:797px;top:0;width:403px;height:574px;background:var(--yellow)}
.contact h2{left:182px;top:75px;font-size:30px;font-weight:500}
.contact p{left:182px;top:131px;width:400px;font-size:14px;line-height:25px;color:var(--muted)}
.field{left:184px;width:361px;height:41px;background:var(--field);font-size:13px;color:#777;padding:13px 18px}

/* footer */
.site-footer{top:3305px;height:240px;background:var(--black);color:var(--white)}
.footer-brand{left:100px;top:78px;display:flex;align-items:center;gap:10px;font-size:17px;font-weight:600;text-transform:uppercase}
.footer-brand .brand-mark{background:var(--white)}
.footer-col{top:52px}
.footer-col h4{font-size:16px;font-weight:500;text-transform:uppercase;margin-bottom:14px}
.footer-col li{list-style:none;font-size:14px;line-height:28px;text-transform:none}
.socials{display:flex;gap:15px;margin-top:2px}
.socials i{width:20px;height:20px;border-radius:50%;background:var(--white);display:block}
</style>
</head>
<body>

<header class="site-header">
  <div class="abs brand"><span class="brand-mark"></span>Brushline Coatings</div>
  <nav>
    <a class="abs nav" style="left:465px">Home</a>
    <a class="abs nav" style="left:535px">Services</a>
    <a class="abs nav" style="left:636px">Gallery</a>
  </nav>
  <div class="abs phone" style="left:766px;top:29px;font-size:16px">
    <svg width="18" height="18" viewBox="0 0 24 24"><path d="M6.6 10.8a15 15 0 0 0 6.6 6.6l2.2-2.2a1 1 0 0 1 1-.25 11 11 0 0 0 3.6.6 1 1 0 0 1 1 1V20a1 1 0 0 1-1 1A17 17 0 0 1 3 4a1 1 0 0 1 1-1h3.5a1 1 0 0 1 1 1c0 1.25.2 2.45.6 3.6a1 1 0 0 1-.25 1z" fill="#000"/></svg>
    1555 0142 78
  </div>
  <a class="btn btn-black" style="left:905px;top:16px;width:182px;height:45px">Get Free Estimate</a>
</header>

<section class="hero" role="img" aria-label="Painters on a lift rolling green paint onto a large grey industrial wall">
  <h1 class="abs">Experienced Local<br>Painting Contractor</h1>
  <a class="btn btn-yellow" style="left:150px;top:231px;width:188px;height:55px">Get Free Estimate</a>
  <svg class="abs" style="left:76px;top:217px" width="22" height="16" viewBox="0 0 22 16"><path d="M21 8H2M8 1 1 8l7 7" stroke="#fff" stroke-width="1.6" fill="none"/></svg>
  <svg class="abs" style="left:1060px;top:224px" width="22" height="16" viewBox="0 0 22 16"><path d="M1 8h19M14 1l7 7-7 7" stroke="#fff" stroke-width="1.6" fill="none"/></svg>
</section>

<section class="about">
  <svg class="abs" style="left:0;top:0" width="600" height="530" viewBox="0 0 600 530">
    <polygon points="227,95 260,95 215,444 470,444 465,462 158,462" fill="var(--yellow)"/>
    <polygon points="242,76 546,76 491,444 186,444" fill="#dfe3ea" role="img" aria-label="Two painters in hard hats rolling white paint onto an interior ceiling"/>
  </svg>
  <h2 class="abs">Business and Commercial<br>Painting Services</h2>
  <p class="abs">Lorem ipsum dolor sit amet consectetur. Sed aenean curabitur sit ultrices enim vitae felis. Mollis mi porttitor diam tristique risus augue malesuada. Semper habitant nunc egestas nulla eget. Aliquet volutpat vitae commodo imperdiet tristique eros eu risus nec.</p>
  <div class="phone">
    <svg width="18" height="18" viewBox="0 0 24 24"><path d="M6.6 10.8a15 15 0 0 0 6.6 6.6l2.2-2.2a1 1 0 0 1 1-.25 11 11 0 0 0 3.6.6 1 1 0 0 1 1 1V20a1 1 0 0 1-1 1A17 17 0 0 1 3 4a1 1 0 0 1 1-1h3.5a1 1 0 0 1 1 1c0 1.25.2 2.45.6 3.6a1 1 0 0 1-.25 1z" fill="#000"/></svg>
    1555 0142 78
  </div>
</section>

<section class="benefits">
  <div class="abs benefit" style="left:200px">
    <svg class="benefit-icon" width="60" height="60" viewBox="0 0 60 60"><polygon points="6,0 60,0 54,60 0,60" fill="#fff"/><rect x="20" y="16" width="20" height="30" fill="#000"/><g fill="#fff"><rect x="23" y="20" width="4" height="4"/><rect x="33" y="20" width="4" height="4"/><rect x="23" y="28" width="4" height="4"/><rect x="33" y="28" width="4" height="4"/><rect x="28" y="38" width="4" height="8"/></g></svg>
    <p>Improve your curb appeal so that you can keep your properties occupied</p>
  </div>
  <div class="abs benefit" style="left:500px">
    <svg class="benefit-icon" width="60" height="60" viewBox="0 0 60 60"><polygon points="6,0 60,0 54,60 0,60" fill="#fff"/><rect x="17" y="30" width="7" height="16" fill="#000"/><path d="M26 30l6-12c3 0 4 2 3 5l-1 5h8c2 0 3 2 2 4l-3 12c0 1-1 2-3 2H26z" fill="#000"/><path d="M40 12l1.5 3 3 1.5-3 1.5-1.5 3-1.5-3-3-1.5 3-1.5z" fill="#000"/></svg>
    <p>Get a beautiful, painless painting experience for you and your tenants</p>
  </div>
  <div class="abs benefit" style="left:782px">
    <svg class="benefit-icon" width="60" height="60" viewBox="0 0 60 60"><polygon points="6,0 60,0 54,60 0,60" fill="#fff"/><path d="M30 14l13 5v9c0 9-6 15-13 18-7-3-13-9-13-18v-9z" fill="#000"/><path d="M24 30l4 4 8-8" stroke="#fff" stroke-width="3" fill="none"/></svg>
    <p>Trust a responsive and responsible partner to get the job done right</p>
  </div>
  <a class="btn btn-black" style="left:506px;top:264px;width:189px;height:56px">Get Free Estimate</a>
</section>

<section class="services">
  <h2 class="abs">Services We Offer</h2>
  <div class="abs service-card" style="left:166px">
    <div class="service-photo" role="img" aria-label="Modern commercial building exterior" style="background:linear-gradient(180deg,#b9c6cf,#a8968a 60%,#6e7a5a)"></div>
    <span>Exterior Painting</span>
  </div>
  <div class="abs service-card" style="left:387px">
    <div class="service-photo" role="img" aria-label="Painted interior with dark feature wall" style="background:linear-gradient(90deg,#8a8c90,#3a3b3e 40%,#55504c 70%,#c5c7c9)"></div>
    <span>Interior Painting</span>
  </div>
  <div class="abs service-card" style="left:607px">
    <div class="service-photo" role="img" aria-label="Glossy epoxy floor in a parking garage" style="background:linear-gradient(180deg,#5b6670,#c3ccd3 55%,#e7ecef)"></div>
    <span>Epoxy Floor Coating</span>
  </div>
  <div class="abs service-card" style="left:827px">
    <div class="service-photo" role="img" aria-label="White coating being rolled onto a roof" style="background:linear-gradient(160deg,#f2f3f4,#d9dcde)"></div>
    <span>Roof Coating</span>
  </div>
  <a class="btn btn-yellow" style="left:506px;top:402px;width:189px;height:55px">View All Services</a>
</section>

<section class="steps">
  <h2 class="abs">How It Works</h2>
  <div class="abs step" style="left:206px">
    <div class="step-icon"><svg width="34" height="34" viewBox="0 0 34 34" fill="none" stroke="#000" stroke-width="1.6"><rect x="4" y="12" width="14" height="18"/><path d="M7 16h8M7 20h2M11 20h2M15 20h0M7 24h2M11 24h2M7 28h2M11 28h2"/><path d="M14 12V4h16v22H18"/><path d="M20 9h6M20 13h6M22 18h4"/></svg></div>
    <div><h3>Step 1</h3><p>Estimator will do a site visit and prepare a scope of work.</p></div>
  </div>
  <div class="abs step" style="left:491px">
    <div class="step-icon"><svg width="34" height="34" viewBox="0 0 34 34" fill="none" stroke="#000" stroke-width="1.6"><rect x="7" y="4" width="20" height="26"/><path d="M11 9h12M11 13h12M11 17h12M11 21h8M11 25h5"/></svg></div>
    <div><h3>Step 2</h3><p>Receive your bid within 24 hours of site visit.</p></div>
  </div>
  <div class="abs step" style="left:762px">
    <div class="step-icon"><svg width="36" height="36" viewBox="0 0 36 36" fill="none" stroke="#000" stroke-width="1.6"><path d="M5 14h16v16H5z"/><path d="M5 14c0-2 16-2 16 0"/><path d="M13 20c-2 3-2 5 0 5s2-2 0-5z"/><path d="M20 12l8-8 4 4-8 8z"/><path d="M24 16l-3 3"/></svg></div>
    <div><h3>Step 3</h3><p>Schedule your start date and let's paint!</p></div>
  </div>
</section>

<section class="cta" role="img" aria-label="Smiling painters in hard hats holding rollers in a bright room">
  <h2 class="abs">We Deliver Extraordinary Experiences</h2>
  <p class="abs">Lorem ipsum dolor sit amet consectetur. Sed aenean curabitur sit ultrices enim vitae felis. Mollis mi porttitor diam tristique risus augue malesuada. Semper habitant nunc egestas nulla eget. Aliquet volutpat vitae commodo imperdiet tristique eros eu risus nec.</p>
  <a class="btn btn-yellow" style="left:524px;top:280px;width:141px;height:56px">Contact Us</a>
</section>

<section class="contact">
  <div class="abs contact-band"></div>
  <h2 class="abs">Contact Us Today!</h2>
  <p class="abs">Lorem ipsum dolor sit amet consectetur. Sed aenean curabitur sit ultrices enim vitae felis. Mollis mi porttitor diam tristique risus augue malesuada.</p>
  <div class="abs field" style="top:211px">Your name</div>
  <div class="abs field" style="top:265px">Phone Number</div>
  <div class="abs field" style="top:318px">Email</div>
  <div class="abs field" style="top:372px">Messages</div>
  <a class="btn btn-send" style="left:183px;top:438px;width:87px;height:57px">Send</a>
  <svg class="abs" style="left:600px;top:0" width="500" height="574" viewBox="600 0 500 574">
    <polygon points="728,104 746,104 688,453 970,453 967,471 665,471" fill="var(--black)"/>
    <polygon points="746,87 1049,87 994,453 688,453" fill="#eceef0" role="img" aria-label="Painter in an orange hard hat rolling pink paint on a white wall"/>
  </svg>
</section>

<footer class="site-footer">
  <div class="abs footer-brand"><span class="brand-mark"></span>Brushline Coatings</div>
  <div class="abs footer-col" style="left:330px">
    <h4>Contact Details</h4>
    <ul><li>Tel: 0155 555 014</li><li>hello@brushlinecoatings.com</li></ul>
  </div>
  <div class="abs footer-col" style="left:600px">
    <h4>Quicklinks</h4>
    <ul><li>HOME</li><li>SERVICES</li><li>GALLERY</li></ul>
  </div>
  <div class="abs footer-col" style="left:842px;top:57px">
    <h4>Connected With Us</h4>
    <div class="socials"><i></i><i></i><i></i><i></i><i></i></div>
  </div>
</footer>

</body>
</html>
```